LETTERHEAD & ENVELOPE: eye-catching stationary design for our custom office furniture business

Our company recently rebranded and we are in need of new stationary. Specifically, we need branded letterhead for standard paper size (8.5” x 11”), and matching envelopes, size: #9.

All designs should incorporate our brand colors, brand typeface, and logo. Please view attached brand guidelines document for brand colors, and brand description.

Letterhead: 8.5” x 11” Must include CoralvexKTN Logo, Dorrit Falke Certified Dealer Logo, mailing address, phone number, website, and email address.

Envelope: 9.5” x 4.125” Must include CoralvexKTN Logo, mailing address, and Dorrit Falke Certified Dealer Logo.

Attached files include:

```html
<!DOCTYPE html>
<html lang="en">
<head>
<meta charset="utf-8">
<title>CoralvexKTN Stationery</title>
<link href="https://fonts.googleapis.com/css2?family=Raleway:wght@300;400&family=Roboto:wght@400&display=swap" rel="stylesheet">
<style>
  :root {
    --backdrop: #c4c4c4;
    --paper: #f5f5f5;
    --brand-green: #5c7e70;
    --ink: #555a58;
    --ink-soft: #6b6f6d;
    --dealer-red: #e8412c;
    --watermark: #e9ebea;
  }
  * { margin: 0; padding: 0; box-sizing: border-box; }
  html, body { width: 1200px; height: 832px; overflow: hidden; background: var(--backdrop); }
  .canvas { position: relative; width: 1200px; height: 832px; }
  .sheet { position: absolute; background: var(--paper); overflow: hidden; box-shadow: 0 1px 3px rgba(0,0,0,.12); }
  .band { position: absolute; left: 0; right: 0; bottom: 0; height: 10px; background: var(--brand-green); }
  .brand { position: absolute; display: flex; align-items: center; }
  .brand-dot { border-radius: 50%; background: var(--brand-green); flex: none; }
  .brand-name { font-family: 'Raleway', sans-serif; font-weight: 400; color: var(--brand-green); letter-spacing: .2px; }
  .address { position: absolute; font-family: 'Roboto', sans-serif; font-size: 7px; line-height: 10px; color: var(--ink); }
  .contact { position: absolute; font-family: 'Roboto', sans-serif; font-size: 7px; line-height: 10px; color: var(--ink); list-style: none; }
  .contact li { display: flex; align-items: center; gap: 4px; }
  .contact svg { width: 7px; height: 7px; fill: var(--ink); }
  .watermark { position: absolute; border-radius: 50%; background: var(--watermark); }
  .dealer { position: absolute; display: flex; align-items: center; gap: 8px; }
  .dealer-badge { width: 23px; height: 23px; border-radius: 50%; background: var(--dealer-red); }
  .dealer-name { font-family: 'Roboto', sans-serif; font-weight: 400; font-size: 11px; color: var(--dealer-red); }

  .letterhead { left: 51px; top: 62px; width: 543px; height: 702px; }
  .letter { position: absolute; left: 56px; top: 197px; width: 428px; font-family: 'Raleway', sans-serif; font-weight: 300; color: var(--ink-soft); }
  .salutation { font-size: 13px; font-weight: 400; margin-bottom: 20px; }
  .letter p.body { font-size: 6.8px; line-height: 10.8px; text-align: justify; margin-bottom: 10.8px; }
  .closing { font-size: 6.8px; margin-top: 18px; }
  .signature { position: absolute; left: 44px; top: 485px; width: 58px; height: 22px; background: linear-gradient(90deg, #dcdcdc, #e8e8e8); border-radius: 3px; }

  .envelope-back { left: 621px; top: 286px; width: 536px; height: 234px; background: var(--paper); }
  .flap { position: absolute; left: 0; top: 0; }
  .envelope-front { left: 621px; top: 533px; width: 537px; height: 233px; }
</style>
</head>
<body>
<div class="canvas">

  <section class="sheet letterhead">
    <div class="watermark" style="left:156px; top:234px; width:228px; height:228px;"></div>
    <div class="brand" style="left:54px; top:63px;">
      <div class="brand-dot" style="width:28px; height:28px; margin-right:9px;"></div>
      <span class="brand-name" style="font-size:22px;">CoralvexKTN</span>
    </div>
    <div class="address" style="left:380px; top:52px;">410 SE Larkmoor, Suite 118<br>Brindlefield, OR 97390</div>
    <ul class="contact" style="left:380px; top:77px;">
      <li><svg viewBox="0 0 10 10"><path d="M2 0h2l1 3-1.5 1a6 6 0 0 0 2.5 2.5L7 5l3 1v2a2 2 0 0 1-2 2A8 8 0 0 1 0 2a2 2 0 0 1 2-2z"/></svg>555.014.2290</li>
      <li><svg viewBox="0 0 10 10"><path d="M0 2h10v6H0z M0 2l5 3.5L10 2" /></svg>info@coralvexktn.com</li>
      <li><svg viewBox="0 0 10 10"><circle cx="5" cy="5" r="5"/></svg>www.coralvexktn.com</li>
    </ul>

    <div class="letter">
      <p class="salutation">Dear Mr. Halvern,</p>
      <p class="body">Lorem ipsum dolor sit amet, consectetur adipiscing elit. Donec orci purus, luctus vitae dignissim eu, iaculis sed purus. Vivamus faucibus, ipsum nec aliquet viverra, leo mauris condimentum ligula, sit amet sagittis enim ligula quis arcu. Nam egestas tortor id nisi porttitor mattis. In tortor ante, ultricies in suscipit a, tempus non massa. Vivamus et auctor mi. Fusce vel massa nulla. Phasellus nec eros mauris, et scelerisque orci.</p>
      <p class="body">Donec malesuada orci vitae nulla accumsan porta a id massa. Quisque accumsan iaculis magna sit amet fringilla. Maecenas consequat, magna eget tincidunt semper, odio nibh rutrum mi, id feugiat ante nisi eu risus. Vestibulum nunc orci, rhoncus a placerat in, ultricies in mi. Cras mattis varius eros, vel fringilla nisi suscipit eget. Quisque scelerisque sagittis nulla at porttitor.</p>
      <p class="body">Sed id augue vitae urna euismod commodo aliquet a quam. Pellentesque arcu velit, cursus et malesuada ut, consequat et diam. Nullam erat sem, rhoncus id ullamcorper vitae, rhoncus et arcu. In ultricies ultricies nulla, ut rutrum nisi iaculis at. Donec eu magna a metus ornare faucibus. Fusce aliquet faucibus ultricies. Morbi semper, est id tincidunt gravida, sem arcu adipiscing lacus, ac bibendum nulla leo eu purus. Quisque nec diam sed risus consectetur a ccumsan quis quis nibh. Vestibulum id purus lorem.</p>
      <p class="body">It is a long established fact that a reader will be distracted by the readable content of a page when looking at its layout. The point of using Lorem Ipsum is that it has a more-or-less normal distribution of letters, as opposed to using 'Content here, content here', making it look like readable English. Many desktop publishing packages</p>
      <p class="closing">Sincerely,</p>
    </div>
    <div class="signature" role="img" aria-label="Handwritten signature"></div>

    <div class="dealer" style="left:174px; top:654px;">
      <div class="dealer-badge"></div>
      <span class="dealer-name">Dorrit Falke Certified Dealer</span>
    </div>
    <div class="band"></div>
  </section>

  <section class="sheet envelope-back">
    <svg class="flap" width="536" height="74" viewBox="0 0 536 74">
      <path d="M0 0H536L526 50Q521 73 498 73H38Q15 73 10 50Z" fill="var(--brand-green)"/>
      <circle cx="268" cy="34" r="16" fill="#ffffff"/>
    </svg>
  </section>

  <section class="sheet envelope-front">
    <div class="watermark" style="left:304px; top:8px; width:216px; height:216px;"></div>
    <div class="brand" style="left:26px; top:27px;">
      <div class="brand-dot" style="width:26px; height:26px; margin-right:8px;"></div>
      <span class="brand-name" style="font-size:21px;">CoralvexKTN</span>
    </div>
    <div class="address" style="left:31px; top:66px;">410 SE Larkmoor, Suite 118<br>Brindlefield, OR 97390</div>
    <div class="dealer" style="left:32px; top:183px;">
      <div class="dealer-badge"></div>
      <span class="dealer-name">Dorrit Falke Certified Dealer</span>
    </div>
    <div class="band"></div>
  </section>

</div>
</body>
</html>
```